Update Business Card Design

I'm looking to update my business cards. Attached is a photo of the current design. I like the black side so that does not have to be update. The white side needs to be updated. I want the design to be modern and minimalistic.
I am a lawyer and my firm's website is www.brennoxlegalco.com (for reference).
My firm's logo has a horizontal version (which is on the black side of the card) and a vertical version (on the white side). I would prefer to keep the vertical version on the white side and horizontal version on the black side (the logo files are attached).

I am open to redesigning the black side also. I would like one side to have the horizontal logo and the other to have the vertical logo.

```html
<!DOCTYPE html>
<html lang="en">
<head>
<meta charset="utf-8">
<title>Brennox Legal Co. — Business Card</title>
<link href="https://fonts.googleapis.com/css2?family=Arimo:wght@400&family=Crimson+Text:wght@400;700&display=swap" rel="stylesheet">
<style>
  :root {
    --backdrop: #4a4a4a;
    --card-dark: #1a1a1b;
    --card-black: #000000;
    --accent: #12b1d9;
    --slate: #4a4b4d;
    --paper: #f3f3f4;
    --ink: #4b4b4d;
    --rule: #5a5a5a;
    --white: #ffffff;
  }
  * { margin: 0; padding: 0; box-sizing: border-box; }
  html, body { width: 1200px; height: 963px; overflow: hidden; }
  body { background: var(--backdrop); position: relative; font-family: "Arimo", Arial, sans-serif; }

  .card { position: absolute; top: 174px; width: 318px; height: 556px; overflow: hidden; }
  .card-front { left: 221px; background: var(--card-dark); }
  .card-back { left: 636px; background: var(--card-black); }

  .card-shapes { position: absolute; inset: 0; }

  /* Front: brand block */
  .brand-mark { position: absolute; left: 178px; top: 58px; width: 86px; height: 86px; border-radius: 50%; background: var(--accent); }
  .brand-rule { position: absolute; left: 157px; top: 167px; width: 132px; height: 1px; background: var(--rule); }
  .brand-name { position: absolute; right: 38px; top: 178px; text-align: right; font-family: "Crimson Text", Georgia, serif; font-weight: 400; color: var(--accent); font-size: 30px; line-height: 30px; letter-spacing: 0.5px; }

  /* Front: name band */
  .person { position: absolute; right: 28px; top: 279px; text-align: right; color: var(--white); }
  .person-name { font-family: "Crimson Text", Georgia, serif; font-weight: 700; font-size: 23px; line-height: 24px; letter-spacing: 0.3px; }
  .person-title { font-size: 14px; line-height: 18px; margin-top: 1px; }

  /* Front: contact list */
  .contact-list { position: absolute; right: 28px; top: 349px; list-style: none; }
  .contact-item { display: flex; align-items: center; justify-content: flex-end; gap: 8px; color: var(--ink); font-size: 13.5px; line-height: 17px; margin-bottom: 6.5px; text-align: right; }
  .contact-item.address { margin-bottom: 6px; }
  .contact-icon { width: 20px; height: 20px; flex: none; }

  .front-web { position: absolute; right: 32px; top: 516px; color: var(--white); font-size: 14px; }

  /* Back */
  .back-name { position: absolute; left: 120px; top: 120px; height: 190px; writing-mode: vertical-rl; transform: rotate(180deg); font-family: "Crimson Text", Georgia, serif; font-weight: 400; color: var(--accent); font-size: 36px; line-height: 40px; text-align: center; white-space: nowrap; }
  .back-rule { position: absolute; left: 117px; top: 313px; width: 84px; height: 1px; background: var(--rule); }
  .back-mark { position: absolute; left: 121px; top: 338px; width: 76px; height: 76px; border-radius: 50%; background: var(--accent); }
  .back-web { position: absolute; left: 236px; top: 110px; height: 336px; writing-mode: vertical-rl; transform: rotate(180deg); font-family: "Crimson Text", Georgia, serif; font-weight: 700; color: var(--white); font-size: 14px; letter-spacing: 2.6px; text-align: center; }
</style>
</head>
<body>

<section class="card card-front" aria-label="Card front">
  <svg class="card-shapes" width="318" height="556" viewBox="0 0 318 556" aria-hidden="true">
    <rect x="0" y="265" width="318" height="74" fill="var(--slate)"/>
    <path d="M50,339 C50,298 74,265 114,265 H318 V339 Z" fill="var(--card-dark)"/>
    <path d="M57,339 C57,301 80,265 121,265 H318 V339 Z" fill="var(--accent)"/>
    <rect x="0" y="339" width="318" height="155" fill="var(--paper)"/>
    <rect x="0" y="494" width="318" height="62" fill="var(--accent)"/>
    <path d="M86,556 C92,518 118,494 160,494 H318 V556 Z" fill="var(--slate)" stroke="var(--white)" stroke-width="5"/>
    <rect x="0" y="496" width="318" height="2" fill="var(--accent)"/>
  </svg>

  <div class="brand-mark" aria-hidden="true"></div>
  <div class="brand-rule"></div>
  <div class="brand-name">BRENNOX<br>LEGAL CO.</div>

  <div class="person">
    <div class="person-name">ADRIAN KESSLER</div>
    <div class="person-title">Attorney at Law</div>
  </div>

  <ul class="contact-list">
    <li class="contact-item address">
      <span>518 Harlow Avenue, Suite 310<br>Westmere, CA 90417</span>
      <svg class="contact-icon" viewBox="0 0 20 20" aria-hidden="true"><circle cx="10" cy="10" r="9" fill="none" stroke="var(--accent)" stroke-width="1.6"/><path d="M10,15.5 C7,11.5 6.5,10 6.5,8.3 A3.5,3.5 0 0 1 13.5,8.3 C13.5,10 13,11.5 10,15.5 Z" fill="none" stroke="var(--accent)" stroke-width="1.4"/><circle cx="10" cy="8.3" r="1.3" fill="var(--accent)"/></svg>
    </li>
    <li class="contact-item">
      <span>555.214.7730</span>
      <svg class="contact-icon" viewBox="0 0 20 20" aria-hidden="true"><circle cx="10" cy="10" r="9" fill="none" stroke="var(--accent)" stroke-width="1.6"/><path d="M6.5,5.5 L8.3,5.3 L9.2,7.8 L8,8.8 C8.7,10.3 9.7,11.3 11.2,12 L12.2,10.8 L14.7,11.7 L14.5,13.5 C10,14 6,10 6.5,5.5 Z" fill="var(--accent)"/></svg>
    </li>
    <li class="contact-item">
      <span>555.214.7731</span>
      <svg class="contact-icon" viewBox="0 0 20 20" aria-hidden="true"><circle cx="10" cy="10" r="9" fill="none" stroke="var(--accent)" stroke-width="1.6"/><rect x="7" y="4.8" width="6" height="10.4" rx="1" fill="none" stroke="var(--accent)" stroke-width="1.4"/><circle cx="10" cy="13.3" r="0.7" fill="var(--accent)"/></svg>
    </li>
    <li class="contact-item">
      <span>555.214.7732</span>
      <svg class="contact-icon" viewBox="0 0 20 20" aria-hidden="true"><circle cx="10" cy="10" r="9" fill="none" stroke="var(--accent)" stroke-width="1.6"/><rect x="7.2" y="5" width="5.6" height="3" fill="var(--accent)"/><rect x="5.3" y="8.5" width="9.4" height="4.5" rx="0.8" fill="var(--accent)"/><rect x="7.2" y="11.5" width="5.6" height="3.5" fill="var(--white)" stroke="var(--accent)" stroke-width="1"/></svg>
    </li>
    <li class="contact-item">
      <span>adrian@BrennoxLegalco.com</span>
      <svg class="contact-icon" viewBox="0 0 20 20" aria-hidden="true"><circle cx="10" cy="10" r="9" fill="none" stroke="var(--accent)" stroke-width="1.6"/><rect x="5.3" y="6.5" width="9.4" height="7" rx="0.6" fill="var(--accent)"/><path d="M5.6,7 L10,10.6 L14.4,7" fill="none" stroke="var(--white)" stroke-width="1"/></svg>
    </li>
  </ul>

  <div class="front-web">BrennoxLegalco.com</div>
</section>

<section class="card card-back" aria-label="Card back">
  <div class="back-name">BRENNOX<br>LEGAL CO.</div>
  <div class="back-rule"></div>
  <div class="back-mark" aria-hidden="true"></div>
  <div class="back-web">WWW.BRENNOXLEGALCO.COM</div>
</section>

</body>
</html>
```